Want to incorporate elements of all these items to make an amazing sign to welcome people to the community. The sign is 6x4 and needs to incorporate the following items:

Welcome to Corwick Meadows

Come visit the PRD sales center at 745 thistledown road
High Speed Fiber Internet
Land financing starting at $299 (No credit checks)
Let us build your dream home!
555-284-7390
We like the gold and black design no teal or blue that was another agents design. Some combination of the current sign all the stuff listed above and then design elements that tie into the truck wrap.

Target Market(s)

People visiting the neighborhood

Industry/Entity Type

real estate and construction

Font styles to use
Serif

Colors

Designer to choose colors to be used in the design.

Requirements
Must have
• PRD Home Builders Welcomes you to Corwick Meadows, Let us build your dream home, Phone number, Land financing starting at $299 NO credit checks

```html
<!DOCTYPE html>
<html lang="en">
<head>
<meta charset="utf-8">
<title>Corwick Meadows Welcome Sign</title>
<link rel="stylesheet" href="https://fonts.googleapis.com/css2?family=Archivo:ital,wght@0,400;0,600;0,700;0,800;1,800&display=swap">
<style>
  :root {
    --backdrop: #3d3d3d;
    --sign-white: #ffffff;
    --ink: #1f201d;
    --gold-light: #e6c860;
    --gold-mid: #d7b54a;
    --gold-deep: #c9a227;
    --gold-text: #d9ae22;
  }
  * { margin: 0; padding: 0; box-sizing: border-box; }
  html, body {
    width: 1200px; height: 1180px; overflow: hidden;
    background: var(--backdrop);
    font-family: "Archivo", Arial, sans-serif;
  }
  .sign {
    position: absolute; left: 40px; top: 220px;
    width: 1120px; height: 740px;
    background: var(--sign-white);
    border-radius: 10px;
    overflow: hidden;
  }
  .welcome-band {
    position: absolute; left: 23px; top: 23px;
    width: 772px; height: 296px;
    background: linear-gradient(180deg, var(--gold-mid) 0%, var(--gold-light) 45%, var(--gold-mid) 100%);
    color: var(--ink);
  }
  .welcome-title {
    position: absolute; left: 32px; top: 28px;
    font-size: 136px; font-weight: 800; line-height: 1;
    letter-spacing: -2px;
  }
  .welcome-place {
    position: absolute; left: 32px; top: 184px;
    font-size: 70px; font-weight: 600; line-height: 1;
    letter-spacing: -1px; white-space: nowrap;
  }
  .fiber-panel {
    position: absolute; left: 795px; top: 23px;
    width: 301px; height: 296px;
    background: var(--ink);
    color: var(--sign-white);
    text-align: center;
  }
  .fiber-top {
    position: absolute; left: 0; right: 0; top: 52px;
    font-size: 37px; font-weight: 700; line-height: 1;
  }
  .fiber-badge {
    position: absolute; left: 33px; top: 100px;
    width: 237px; height: 88px;
    background: linear-gradient(180deg, var(--gold-mid), var(--gold-light), var(--gold-mid));
    color: var(--ink);
    font-size: 72px; font-weight: 700; line-height: 88px;
  }
  .fiber-bottom {
    position: absolute; left: 0; right: 0; top: 220px;
    font-size: 35px; font-weight: 700; line-height: 1;
    letter-spacing: 6px; padding-left: 6px;
  }
  .builder-name {
    position: absolute; left: 40px; top: 380px;
    display: flex; align-items: center; gap: 16px;
    color: var(--ink);
    font-size: 40px; font-weight: 700; line-height: 1;
    white-space: nowrap;
  }
  .builder-mark {
    width: 52px; height: 52px;
    background: var(--gold-deep);
  }
  .sales-center {
    position: absolute; left: 520px; top: 362px;
    color: var(--ink);
  }
  .sales-line {
    font-size: 36px; font-weight: 600; line-height: 1; white-space: nowrap;
  }
  .sales-address {
    margin-top: 22px;
    font-size: 32px; font-weight: 600; line-height: 1; white-space: nowrap;
  }
  .sales-address strong { font-size: 46px; font-weight: 700; }
  .info-band {
    position: absolute; left: 0; top: 508px;
    width: 1120px; height: 120px;
    background: var(--ink);
    color: var(--sign-white);
  }
  .financing {
    position: absolute; left: 43px; top: 20px;
    font-size: 36px; font-weight: 400; line-height: 1.2;
  }
  .financing .price { font-weight: 800; }
  .financing .note { color: var(--gold-text); }
  .phone {
    position: absolute; left: 527px; top: 22px;
    display: flex; align-items: center; gap: 16px;
    color: var(--gold-text);
    font-size: 72px; font-weight: 700; line-height: 1;
  }
  .phone svg { width: 40px; height: 40px; margin-top: 8px; }
  .tagline {
    position: absolute; left: 0; right: 0; top: 650px;
    text-align: center;
    color: var(--ink);
    font-size: 47px; font-weight: 400; line-height: 1;
  }
  .tagline em { font-weight: 800; font-style: italic; }
</style>
</head>
<body>
  <main class="sign">
    <section class="welcome-band">
      <h1 class="welcome-title">WELCOME</h1>
      <p class="welcome-place">to Corwick Meadows</p>
    </section>
    <aside class="fiber-panel">
      <p class="fiber-top">HIGH SPEED</p>
      <p class="fiber-badge">FIBER</p>
      <p class="fiber-bottom">INTERNET</p>
    </aside>
    <p class="builder-name"><span class="builder-mark" aria-hidden="true"></span>PRD Home Builders</p>
    <div class="sales-center">
      <p class="sales-line">Come visit the PRD sales center</p>
      <p class="sales-address">at <strong>745 Thistledown Road</strong></p>
    </div>
    <section class="info-band">
      <p class="financing">Land financing starting at<br><span class="price">$299</span> <span class="note">(No credit checks)</span></p>
      <p class="phone">
        <svg viewBox="0 0 24 24" aria-hidden="true"><path fill="#ffffff" d="M6.6 10.8c1.4 2.8 3.8 5.1 6.6 6.6l2.2-2.2c.3-.3.7-.4 1-.2 1.1.4 2.3.6 3.6.6.6 0 1 .4 1 1V20c0 .6-.4 1-1 1C10.6 21 3 13.4 3 4c0-.6.4-1 1-1h3.5c.6 0 1 .4 1 1 0 1.3.2 2.5.6 3.6.1.3 0 .7-.2 1L6.6 10.8z"/></svg>
        555-284-7390
      </p>
    </section>
    <p class="tagline">LET US BUILD YOUR <em>DREAM HOME!</em></p>
  </main>
</body>
</html>
```